Copper Ridge Upkeep and Errand Flyer

We need a flyer for copper ridge upkeep and errand service. We specialize in and provide residential maintenance and errand services to retired and semi retired persons living in the Lake Norman area. The services we include:
Lighting and plumbing repairs
Ceiling fan installation
Handicap accessories
Locks and security
Picture hanging
Hang blinds
Furniture arrangement / assembly
Pressure washing
Battery Jump start
and more...

Our Concierge services include:
Errand running
Grocery shopping
Wellness Checks
Dog Walk
Garbage Collection
and more...

We offer monthly service agreements and 24/7 access
Call text or e-mail for more information
555.418.2963
1copperridgeupk@quillbox-mail.net

The design should invoke a sense of trust and a customer service driven mission

Target Market(s)

Residential maintenance

Industry/Entity Type

Property Maintenance

Contact Information for Business Card

Dale Hurst
20814 Fennick Gale Rd.
Cornelius NC 28947
555.418.2963
with uploaded logo

Requirements
Nice to have
• Would like a postcard size flyer. Front and back
Should not have
• No pics of of people wearing hard hats or pics of blueprints. No pics of commercial or industrial maintenance.

```html
<!DOCTYPE html>
<html lang="en">
<head>
<meta charset="utf-8">
<title>Copper Ridge Upkeep and Errand Flyer</title>
<link href="https://fonts.googleapis.com/css2?family=Questrial&family=Oswald:wght@300;400&display=swap" rel="stylesheet">
<style>
  :root {
    --red: #d0202a;
    --ink: #1e1e1e;
    --grey: #5a5a5a;
    --cream-top: #fdf3ee;
    --cream-bottom: #fbe9e1;
    --backdrop: #2b2b2b;
  }
  * { margin: 0; padding: 0; box-sizing: border-box; }
  html, body { width: 1200px; height: 900px; overflow: hidden; }
  body { background: var(--backdrop); position: relative; font-family: "Questrial", sans-serif; color: var(--ink); }

  .flyer {
    position: absolute; top: 82px; width: 526px; height: 735px;
    background: linear-gradient(180deg, var(--cream-top), var(--cream-bottom));
    overflow: hidden;
  }
  .flyer--front { left: 54px; }
  .flyer--back { left: 621px; }
  .flyer > * { position: absolute; }
  .flyer .art { left: 0; top: 0; width: 526px; height: 735px; }

  .brand { left: 36px; top: 28px; display: flex; align-items: center; gap: 10px; }
  .brand-dot { width: 44px; height: 44px; border-radius: 50%; border: 5px solid var(--red); }
  .brand-name { font-size: 17px; line-height: 21px; color: var(--grey); width: 190px; }

  .access { right: 30px; top: 30px; font-family: "Oswald", sans-serif; font-weight: 300; font-size: 19px; }
  .phone-line { display: flex; align-items: center; gap: 8px; font-family: "Oswald", sans-serif; font-weight: 300; font-size: 22px; }
  .flyer--front .top-phone { right: 30px; top: 58px; }
  .flyer--back .top-phone { right: 30px; top: 46px; }
  .phone-icon { width: 22px; height: 22px; }

  .intro { left: 0; width: 526px; top: 504px; text-align: center; font-size: 19px; line-height: 25px; }
  .offer { left: 0; width: 526px; top: 597px; text-align: center; font-size: 19px; line-height: 24px; }
  .offer .accent { color: var(--red); }
  .contact-phone { left: 0; width: 526px; top: 648px; justify-content: center; font-family: "Questrial", sans-serif; font-size: 25px; }
  .contact-phone .phone-icon { width: 24px; height: 24px; }
  .contact-email { left: 0; width: 526px; top: 680px; display: flex; justify-content: center; align-items: center; gap: 8px; font-size: 18px; }

  .ribbon {
    background: var(--red); color: #fff; font-family: "Oswald", sans-serif; font-weight: 300;
    display: flex; align-items: center;
  }
  .ribbon--services { left: 0; top: 430px; width: 231px; height: 32px; padding-left: 26px; font-size: 20px; border-radius: 0 6px 6px 0; }
  .ribbon--concierge { left: 284px; top: 506px; width: 242px; height: 32px; padding-left: 24px; font-size: 18px; border-radius: 6px 0 0 6px; }

  .service-list { list-style: none; font-size: 17px; line-height: 23.7px; }
  .service-list li { display: flex; align-items: flex-start; gap: 8px; }
  .service-list li::before {
    content: ""; flex: none; width: 10px; height: 10px; margin-top: 7px;
    border-radius: 50%; border: 2px solid var(--red); background: #fff;
  }
  .service-list .more { font-size: 15px; margin-left: 20px; }
  .service-list .more-line::before { visibility: hidden; }
  .list--services { left: 27px; top: 472px; width: 280px; }
  .list--concierge { left: 307px; top: 548px; width: 200px; }
  .list--services .inline-more { font-size: 14px; margin-left: 20px; }

  .base-band { left: 0; bottom: 0; width: 526px; height: 17px; background: var(--red); }
</style>
</head>
<body>

<section class="flyer flyer--front">
  <svg class="art" viewBox="0 0 526 735" aria-hidden="false">
    <defs>
      <linearGradient id="portraitTone" x1="0" y1="0" x2="1" y2="1">
        <stop offset="0" stop-color="#e4e8ec"/>
        <stop offset="0.55" stop-color="#b9c2cc"/>
        <stop offset="1" stop-color="#f1f2f4"/>
      </linearGradient>
      <radialGradient id="bellTone" cx="0.5" cy="0.6" r="0.6">
        <stop offset="0" stop-color="#c9c9cc"/>
        <stop offset="1" stop-color="#ffffff"/>
      </radialGradient>
    </defs>
    <circle cx="172" cy="303" r="180" fill="var(--red)"/>
    <g role="img" aria-label="Photo of a friendly service technician holding a clipboard">
      <rect x="150" y="133" width="376" height="285" fill="url(#portraitTone)"/>
      <circle cx="182" cy="300" r="165" fill="url(#portraitTone)"/>
    </g>
    <circle cx="408" cy="340" r="113" fill="var(--red)"/>
    <circle cx="414" cy="336" r="105" fill="url(#bellTone)" role="img" aria-label="Photo of a finger pressing a silver service bell"/>
  </svg>

  <div class="brand">
    <span class="brand-dot"></span>
    <span class="brand-name">Copper Ridge Upkeep and Errand</span>
  </div>

  <p class="access">We Offer 24/7 Access</p>
  <p class="phone-line top-phone">
    <svg class="phone-icon" viewBox="0 0 24 24"><circle cx="12" cy="12" r="10.5" fill="none" stroke="var(--red)" stroke-width="2"/><path d="M8.5 6.5l2 2.2-1.2 1.5c.8 1.7 2 2.9 3.5 3.6l1.5-1.2 2.2 2-1.2 1.8c-3.8-.4-7.4-4-7.7-7.8z" fill="var(--red)"/></svg>
    555.418.2963
  </p>

  <p class="intro">We specialize in and provide residential<br>maintenance and errand services to retired and semi<br>retired persons living in the Lake Norman area.</p>
  <p class="offer">We offer monthly service agreements and <span class="accent">24/7 access</span><br>Call text or e-mail for more information</p>
  <p class="phone-line contact-phone">
    <svg class="phone-icon" viewBox="0 0 24 24"><circle cx="12" cy="12" r="10.5" fill="none" stroke="var(--red)" stroke-width="2"/><path d="M8.5 6.5l2 2.2-1.2 1.5c.8 1.7 2 2.9 3.5 3.6l1.5-1.2 2.2 2-1.2 1.8c-3.8-.4-7.4-4-7.7-7.8z" fill="var(--red)"/></svg>
    555.418.2963
  </p>
  <p class="contact-email">
    <svg width="18" height="13" viewBox="0 0 18 13"><rect x="0.75" y="0.75" width="16.5" height="11.5" fill="none" stroke="var(--red)" stroke-width="1.5"/><path d="M1 1l8 6.5L17 1" fill="none" stroke="var(--red)" stroke-width="1.5"/></svg>
    1copperridgeupk@quillbox-mail.net
  </p>

  <div class="base-band"></div>
</section>

<section class="flyer flyer--back">
  <svg class="art" viewBox="0 0 526 735">
    <defs>
      <linearGradient id="repairTone" x1="0" y1="0" x2="1" y2="1">
        <stop offset="0" stop-color="#f2f3f5"/>
        <stop offset="0.6" stop-color="#c8ccd2"/>
        <stop offset="1" stop-color="#8a93a2"/>
      </linearGradient>
    </defs>
    <circle cx="344" cy="290" r="188" fill="var(--red)"/>
    <g role="img" aria-label="Photo of a technician repairing plumbing under a sink">
      <rect x="0" y="118" width="344" height="340" fill="url(#repairTone)"/>
      <circle cx="336" cy="284" r="176" fill="url(#repairTone)"/>
    </g>
  </svg>

  <div class="brand">
    <span class="brand-dot"></span>
    <span class="brand-name">Copper Ridge Upkeep and Errand</span>
  </div>

  <p class="phone-line top-phone">
    <svg class="phone-icon" viewBox="0 0 24 24"><circle cx="12" cy="12" r="10.5" fill="none" stroke="var(--red)" stroke-width="2"/><path d="M8.5 6.5l2 2.2-1.2 1.5c.8 1.7 2 2.9 3.5 3.6l1.5-1.2 2.2 2-1.2 1.8c-3.8-.4-7.4-4-7.7-7.8z" fill="var(--red)"/></svg>
    555.418.2963
  </p>

  <h2 class="ribbon ribbon--services">The services we include:</h2>
  <ul class="service-list list--services">
    <li>Lighting and plumbing repairs</li>
    <li>Ceiling fan installation</li>
    <li>Handicap accessories</li>
    <li>Locks and security</li>
    <li>Picture hanging</li>
    <li>Hang blinds</li>
    <li>Furniture arrangement /<br>assembly</li>
    <li>Pressure washing</li>
    <li>Battery Jump start <span class="inline-more">and more...</span></li>
  </ul>

  <h2 class="ribbon ribbon--concierge">Our Concierge services include:</h2>
  <ul class="service-list list--concierge">
    <li>Errand running</li>
    <li>Grocery shopping</li>
    <li>Wellness Checks</li>
    <li>Dog Walk</li>
    <li>Garbage Collection</li>
    <li class="more-line">and more...</li>
  </ul>

  <div class="base-band"></div>
</section>

</body>
</html>
```